Lantern Co. Supplement General Packaging Design

I am looking for a design template to design all of my various supplements and other products around. Meaning that this design should be able to just be able to change around words, up to a few small images, and text to suit my other various products.

The brand name is Lantern Co. and the slogan is: Legends Take Root
This is For an Apple Cider Vinegar Gummy, and include these top three things: Vegan, Gluten Free, Non-GMO somewhere in the design.

I want the design to have a luxurious feel. With some kind of design element where the logo is sort of the secondary aspect of the design.

Target Market(s)

Men age 24-45

Industry/Entity Type

Supplement

Requirements
Must have
• MUST HAVE A "vintage" LOOK AND FEEL. MUST HAVE ANOTHER design element besides the logo. (Something Vintage) MUST USE THE PROVIDED TEMPLATE A PDF IN THE FILES BELOW LABELED " TEMPLATE" and the LOGO PROVIDED under "Lantern Co. 2" OR "Lantern Co.3" whichever is better suited for the design. Bold design. Another color besides black to stand out. Use the lantern co logo which is below in the provided images. The design should go around the logo and fit the same aesthetic. The rest are for inspiration, what I like.

```html
<!DOCTYPE html>
<html lang="en">
<head>
<meta charset="utf-8">
<title>Lantern Co. Supplement Label</title>
<link rel="stylesheet" href="https://fonts.googleapis.com/css2?family=Poppins:wght@500;600&display=swap">
<style>
  :root {
    --page-bg: #ffffff;
    --silver-dark: #4a4a4a;
    --silver-mid: #9a9a9a;
    --silver-light: #f4f4f4;
    --navy-deep: #0a1a33;
    --navy-bright: #1b3763;
    --ink-slate: #1b2733;
    --ink-night: #0a1926;
    --label-text: #ffffff;
    --rule: rgba(255, 255, 255, 0.45);
    --rule-soft: rgba(255, 255, 255, 0.22);
  }
  html, body {
    margin: 0;
    padding: 0;
    width: 1200px;
    height: 786px;
    overflow: hidden;
    background: var(--page-bg);
  }
  .canvas {
    position: relative;
    width: 1200px;
    height: 786px;
  }
  .label {
    position: absolute;
    left: 50px;
    top: 164px;
    width: 1100px;
    height: 458px;
    background: linear-gradient(90deg,
      #5a5a5a 0%,
      #bdbdbd 22%,
      var(--silver-light) 36%,
      var(--silver-mid) 52%,
      #6a6a6a 66%,
      var(--silver-dark) 80%,
      #adadad 100%);
  }
  .label-panel {
    position: absolute;
    left: 0;
    top: 37px;
    width: 833px;
    height: 389px;
    border-radius: 0 170px 170px 0;
    background: linear-gradient(90deg,
      var(--navy-deep) 0%,
      var(--navy-bright) 25%,
      var(--navy-bright) 31%,
      #1c2a3d 44%,
      var(--ink-slate) 58%,
      var(--ink-night) 100%);
  }
  .panel-frame {
    position: absolute;
    inset: 12px 12px 12px 12px;
    border: 1px solid var(--rule);
    border-left: none;
    border-radius: 0 158px 158px 0;
    pointer-events: none;
  }
  .panel-frame-inner {
    position: absolute;
    inset: 18px 18px 18px 18px;
    border: 1px solid var(--rule-soft);
    border-left: none;
    border-radius: 0 152px 152px 0;
    pointer-events: none;
  }
  .brand-name {
    position: absolute;
    left: 100px;
    top: 58px;
    margin: 0;
    font-family: "Poppins", sans-serif;
    font-weight: 600;
    font-size: 108px;
    line-height: 1;
    letter-spacing: -0.01em;
    color: var(--label-text);
    white-space: nowrap;
  }
  .tagline {
    position: absolute;
    left: 104px;
    top: 198px;
    margin: 0;
    font-family: "Poppins", sans-serif;
    font-weight: 600;
    font-size: 33px;
    line-height: 1;
    letter-spacing: 0.46em;
    color: var(--label-text);
    white-space: nowrap;
  }
  .divider {
    position: absolute;
    left: 104px;
    top: 256px;
    width: 556px;
    height: 5px;
    border-top: 1px solid var(--rule);
    border-bottom: 1px solid var(--rule-soft);
  }
  .product-name {
    position: absolute;
    left: 104px;
    top: 276px;
    margin: 0;
    font-family: "Poppins", sans-serif;
    font-weight: 500;
    font-size: 22px;
    line-height: 1;
    letter-spacing: 0.22em;
    text-transform: uppercase;
    color: var(--label-text);
    white-space: nowrap;
  }
  .claims {
    position: absolute;
    left: 104px;
    top: 322px;
    margin: 0;
    padding: 0;
    list-style: none;
    display: flex;
    gap: 34px;
    font-family: "Poppins", sans-serif;
    font-weight: 500;
    font-size: 15px;
    line-height: 1;
    letter-spacing: 0.16em;
    text-transform: uppercase;
    color: var(--label-text);
    white-space: nowrap;
  }
  .claim {
    display: flex;
    align-items: center;
    gap: 9px;
  }
  .claim-tick {
    width: 16px;
    height: 16px;
    flex: none;
  }
</style>
</head>
<body>
  <main class="canvas">
    <section class="label" aria-label="Lantern Co. product label">
      <div class="label-panel">
        <div class="panel-frame"></div>
        <div class="panel-frame-inner"></div>
        <h1 class="brand-name">Lantern Co</h1>
        <p class="tagline">Legends Take Root</p>
        <div class="divider"></div>
        <h2 class="product-name">Apple Cider Vinegar Gummies</h2>
        <ul class="claims">
          <li class="claim">
            <svg class="claim-tick" viewBox="0 0 16 16" aria-hidden="true"><circle cx="8" cy="8" r="7.2" fill="none" stroke="#ffffff" stroke-width="1.2"/><path d="M4.6 8.3l2.2 2.2 4.6-4.8" fill="none" stroke="#ffffff" stroke-width="1.5" stroke-linecap="round" stroke-linejoin="round"/></svg>
            Vegan
          </li>
          <li class="claim">
            <svg class="claim-tick" viewBox="0 0 16 16" aria-hidden="true"><circle cx="8" cy="8" r="7.2" fill="none" stroke="#ffffff" stroke-width="1.2"/><path d="M4.6 8.3l2.2 2.2 4.6-4.8" fill="none" stroke="#ffffff" stroke-width="1.5" stroke-linecap="round" stroke-linejoin="round"/></svg>
            Gluten Free
          </li>
          <li class="claim">
            <svg class="claim-tick" viewBox="0 0 16 16" aria-hidden="true"><circle cx="8" cy="8" r="7.2" fill="none" stroke="#ffffff" stroke-width="1.2"/><path d="M4.6 8.3l2.2 2.2 4.6-4.8" fill="none" stroke="#ffffff" stroke-width="1.5" stroke-linecap="round" stroke-linejoin="round"/></svg>
            Non-GMO
          </li>
        </ul>
      </div>
    </section>
  </main>
</body>
</html>
```